Brindlewood Lamb - Online retail of "Meadow to Table" lamb

Design and publish our website that is google tracking friendly, SEO friendly and also allows a good shop using paylune payments.
Current website is www.brwdmeats.com.au. All the information and data is on there. for copy past.
Also include a recipe page. not a blog, but actual recipes we can change for seasons. i.e. hearty winter meals, v summer light and playful food.
We don't want anything complex, it needs to feel trustworthy, not to busy. make it easy to click and buy.

I also want to be able to update and manage myself once running, to reduce overheads.

Also ability to link post vane to the signup/contact information

Target Market(s)

people looking to save money and pay $15/kg, instead of supermarket chain $45/kg. People who like fresh, ethically grown produce.

Industry/Entity Type

Primary producer, Food

Coding

Coded - Design and coding required

Number of Pages Required

4 page

Font styles to use
Other font styles liked:
• Im not sure.

Requirements
Must have
• Easy functionality, trust worthy and easy use store/ordering, google tracking compatiable.
Nice to have
• Subscription, IE client signs up for a Half/Side of lamb delivered monthly for subscription fee

```html
<!DOCTYPE html>
<html lang="en">
<head>
<meta charset="utf-8">
<title>Brindlewood Farms – Meadow to Table Lamb</title>
<link href="https://fonts.googleapis.com/css2?family=Barlow:wght@600;700&family=Open+Sans:wght@400;600&display=swap" rel="stylesheet">
<style>
:root{
  --red:#d44848;
  --ink:#1c1c1c;
  --text:#3a3a3a;
  --cream:#fcf8f3;
  --cream-box:#faf4e6;
  --line:#ececec;
  --footer:#1f1f21;
  --footer-bar:#2a2a2c;
  --white:#ffffff;
}
*{box-sizing:border-box;margin:0;padding:0}
html,body{width:1200px;height:3467px;overflow:hidden;background:var(--white)}
body{position:relative;font-family:"Open Sans",sans-serif;color:var(--text)}
.abs{position:absolute}
.btn{position:absolute;display:flex;align-items:center;justify-content:center;background:var(--red);color:var(--white);border-radius:30px;font-size:16px;font-weight:600}
h2{font-family:"Barlow",sans-serif;font-weight:700;color:var(--ink);letter-spacing:.5px;font-size:44px;line-height:1}

/* header */
.site-header{left:0;top:0;width:1200px;height:102px;background:var(--white)}
.brand{left:112px;top:18px;display:flex;align-items:center;gap:10px;font-family:"Open Sans",sans-serif;font-weight:600;font-size:15px;color:var(--ink)}
.brand-dot{width:62px;height:62px;border-radius:50%;border:2px solid var(--ink)}
.nav{left:417px;top:38px;display:flex;gap:36px;font-size:15.5px;color:#444}
.nav .active{color:var(--ink);font-weight:600}

/* hero */
.hero{left:0;top:102px;width:1200px;height:470px;background:linear-gradient(180deg,#6d6a55 0%,#a9a28e 35%,#c5bfae 55%,#6f8a3c 85%,#5a7a2e 100%)}
.hero-welcome{left:0;width:1200px;top:336px;text-align:center;color:var(--white);font-size:32px}
.hero-title{left:0;width:1200px;top:390px;text-align:center;color:var(--white);font-family:"Barlow",sans-serif;font-weight:700;font-size:58px;letter-spacing:.5px}

/* story */
.story-text p{font-size:15px;line-height:28.5px;text-align:justify;color:#444}
.story-img{left:660px;top:638px;width:428px;height:384px;border-radius:4px;background:linear-gradient(180deg,#b9c3cc 0%,#8fa17a 45%,#cfcab8 70%,#7d8c52 100%)}

/* why */
.why{left:112px;top:1091px;width:976px;height:388px;background:var(--cream-box);border:1px solid #efe6d2;border-radius:6px;text-align:center}
.why p{font-size:15.5px;line-height:28px;color:var(--ink)}
.why strong{color:var(--red)}

/* products */
.card{top:1648px;width:305px;height:413px;border:1px solid var(--line);border-radius:10px;background:var(--white)}
.card-img{position:absolute;left:10px;top:10px;width:285px;height:279px;border-radius:4px;background:linear-gradient(160deg,#6b4a36 0%,#b57a74 40%,#d9a6a3 60%,#5b3a28 100%)}
.card-title{position:absolute;left:19px;top:308px;width:270px;font-size:15.5px;line-height:26px;color:var(--ink)}
.card-price{position:absolute;left:17px;top:368px;font-size:16.5px;font-weight:600;color:var(--red)}

/* recipes */
.recipes{left:0;top:2218px;width:1200px;height:533px;background:var(--cream)}
.recipe-img-a{left:112px;top:2297px;width:302px;height:277px;background:linear-gradient(150deg,#2a2320 0%,#6a4a3a 50%,#1f1a18 100%)}
.recipe-img-b{left:293px;top:2479px;width:258px;height:215px;border:9px solid var(--white);background:linear-gradient(150deg,#2a2320 0%,#5c3a2c 50%,#9a5a2e 80%,#231d1a 100%)}
.recipes p{font-size:15px;line-height:28.5px;text-align:justify;color:#444}

/* subscribe */
.sub-form{left:290px;top:2962px;width:620px;height:59px;border-radius:30px;background:var(--white);box-shadow:0 2px 10px rgba(0,0,0,.1)}

/* footer */
.footer{left:0;top:3140px;width:1200px;height:327px;background:var(--footer)}
.footer h4{font-size:17px;font-weight:600;color:var(--white);letter-spacing:.5px}
.footer .item{font-size:15.5px;color:#f0f0f0;line-height:30px}
.divider{width:1px;height:40px;background:#555}
.copyright{left:0;top:3424px;width:1200px;height:43px;background:var(--footer-bar);color:#aaa;font-size:14px;display:flex;align-items:center;justify-content:center}
.partner{font-family:"Open Sans",sans-serif;font-weight:600;color:var(--white)}
</style>
</head>
<body>

<header class="abs site-header">
  <div class="abs brand"><span class="brand-dot"></span>Brindlewood Farms</div>
  <nav class="abs nav">
    <span class="active">Home</span><span>About Us</span><span>Products</span><span>Recipes</span><span>Contact Us</span>
  </nav>
  <a class="btn" style="left:909px;top:30px;width:179px;height:43px">Order Fresh Lambs</a>
</header>

<section>
  <div class="abs hero" role="img" aria-label="Flock of woolly sheep grazing in a green paddock"></div>
  <svg class="abs" style="left:0;top:520px" width="1200" height="60" viewBox="0 0 1200 60" aria-hidden="true">
    <path d="M0 15 L40 22 L90 18 L140 28 L200 20 L260 30 L320 24 L380 34 L440 28 L500 38 L560 30 L620 36 L680 26 L740 30 L800 22 L860 26 L920 18 L980 24 L1040 16 L1100 22 L1160 14 L1200 18 L1200 60 L0 60 Z" fill="#fff"/>
  </svg>
  <div class="abs hero-welcome">Welcome to</div>
  <div class="abs hero-title">BRINDLEWOOD FARMS!</div>
</section>

<section>
  <h2 class="abs" style="left:112px;top:656px">OUR STORY</h2>
  <div class="abs story-text" style="left:112px;top:726px;width:488px">
    <p>Our journey began in the heart of Mount Harlow, WA, where lush pastures and happy sheep set the scene for our vision. We dreamed of a place where the soft bleats of lambs echo through the fields, and where the love for premium lamb cuts meets the warmth of a close-knit community.</p>
    <p style="margin-top:12px;text-align:left;color:var(--ink)">Brindlewood Lamb Haven was born from this dream, and it's been a woolly adventure ever since!</p>
  </div>
  <a class="btn" style="left:112px;top:974px;width:137px;height:43px">Learn More</a>
  <div class="abs story-img" role="img" aria-label="Farmer feeding sheep from a bucket in an open paddock"></div>
</section>

<section class="abs why">
  <h2 style="margin-top:64px">WHY OUR LAMB</h2>
  <p style="margin:34px auto 0;width:580px">Our targets are people looking to save money and pay <strong>$15/kg</strong>, instead of the supermarket chain $45/kg.</p>
  <p style="margin-top:6px">People who like fresh, ethically grown produce.</p>
  <a class="btn" style="left:397px;top:284px;width:181px;height:43px">Order Fresh Lambs</a>
</section>

<section>
  <h2 class="abs" style="left:0;width:1200px;top:1556px;text-align:center">OUR PRODUCTS</h2>
  <div class="abs card" style="left:113px">
    <div class="card-img" role="img" aria-label="Packed lamb prime cuts on a wooden table"></div>
    <div class="card-title">Fresh Whole Lamb Prime Cut Pack- $16.50 per kg</div>
    <div class="card-price">$100</div>
  </div>
  <div class="abs card" style="left:448px">
    <div class="card-img" role="img" aria-label="Packed side of lamb cuts on a wooden table"></div>
    <div class="card-title">Fresh Side of Lamb Prime Cut Pack- $16.50 per kg</div>
    <div class="card-price">$100</div>
  </div>
  <div class="abs card" style="left:783px">
    <div class="card-img" role="img" aria-label="Packed lamb chops and roasts on a wooden table"></div>
    <div class="card-title">Fresh Whole Lamb - Chops and Roast Pack - $15 per kg</div>
    <div class="card-price">$100</div>
  </div>
  <a class="btn" style="left:540px;top:2113px;width:121px;height:42px">View All</a>
</section>

<section>
  <div class="abs recipes"></div>
  <div class="abs recipe-img-a" role="img" aria-label="Roasted rack of lamb with vegetables"></div>
  <div class="abs recipe-img-b" role="img" aria-label="Slow roasted lamb shoulder with herbs"></div>
  <h2 class="abs" style="left:600px;top:2312px">RECIPES</h2>
  <div class="abs" style="left:600px;top:2380px;width:488px">
    <p>Sed ut perspiciatis unde omnis iste natus error sit voluptatem accusantium doloremque laudantium, totam rem aperiam, eaque ipsa quae ab illo inventore veritatis et quasi architecto beatae vitae dicta sunatem qequuntur mag voluptatem sequi nesciunt. Neque porro quisquam est, qui dolorem ipsum quia dolor.</p>
    <p style="margin-top:12px;color:var(--ink)">Ut enim ad minima veniam, quis nostrum exercitationem ullam corporis suscipit laboriosam, nisi ut aliquid</p>
  </div>
  <a class="btn" style="left:600px;top:2630px;width:137px;height:42px">Check Out</a>
</section>

<section>
  <h2 class="abs" style="left:0;width:1200px;top:2842px;text-align:center">SUBSCRIBE TO US</h2>
  <div class="abs" style="left:0;width:1200px;top:2907px;text-align:center;font-size:16px;color:var(--ink)">Sign up for a Half/Side of lamb delivered monthly for subscription fee</div>
  <div class="abs sub-form">
    <span class="abs" style="left:35px;top:19px;font-size:15.5px;color:#888">Email Address</span>
    <a class="btn" style="left:432px;top:8px;width:180px;height:43px">Subscribe Now!</a>
  </div>
</section>

<footer>
  <svg class="abs" style="left:0;top:3098px" width="1200" height="46" viewBox="0 0 1200 46" aria-hidden="true">
    <path d="M0 46 L0 38 L50 34 L110 36 L170 28 L240 30 L310 22 L380 20 L450 14 L520 12 L560 6 L620 8 L680 12 L740 16 L800 22 L860 24 L920 30 L990 28 L1060 34 L1130 32 L1200 36 L1200 46 Z" fill="#1f1f21"/>
  </svg>
  <div class="abs footer">
    <div class="abs" style="left:112px;top:78px;display:flex;align-items:center;gap:12px">
      <span style="width:70px;height:70px;border-radius:50%;border:2px solid #fff;display:block"></span>
      <span class="partner" style="font-size:18px">Brindlewood<br>Farms</span>
    </div>

    <h4 class="abs" style="left:426px;top:60px">CONTACTS</h4>
    <svg class="abs" style="left:426px;top:106px" width="16" height="20" viewBox="0 0 16 20" aria-hidden="true"><path d="M8 0a7 7 0 0 0-7 7c0 5 7 13 7 13s7-8 7-13a7 7 0 0 0-7-7zm0 9.5A2.5 2.5 0 1 1 8 4.5a2.5 2.5 0 0 1 0 5z" fill="#d44848"/></svg>
    <div class="abs item" style="left:461px;top:100px">Brindlewood Farms,<br>Address Comes Here</div>
    <svg class="abs" style="left:426px;top:174px" width="17" height="17" viewBox="0 0 24 24" aria-hidden="true"><path d="M6.6 10.8a15.1 15.1 0 0 0 6.6 6.6l2.2-2.2a1 1 0 0 1 1-.25 11.4 11.4 0 0 0 3.6.57 1 1 0 0 1 1 1V20a1 1 0 0 1-1 1A17 17 0 0 1 3 4a1 1 0 0 1 1-1h3.5a1 1 0 0 1 1 1c0 1.25.2 2.45.57 3.6a1 1 0 0 1-.25 1z" fill="#d44848"/></svg>
    <div class="abs item" style="left:461px;top:167px">0400 218 604</div>
    <svg class="abs" style="left:426px;top:223px" width="18" height="14" viewBox="0 0 18 14" aria-hidden="true"><rect width="18" height="14" rx="2" fill="#d44848"/><path d="M1 2l8 6 8-6" stroke="#1f1f21" stroke-width="1.6" fill="none"/></svg>
    <div class="abs item" style="left:461px;top:214px">hello@brwdmeats.com.au</div>

    <div class="abs divider" style="left:677px;top:135px"></div>

    <h4 class="abs" style="left:752px;top:60px">QUICK LINKS</h4>
    <div class="abs item" style="left:752px;top:100px">Home<br>About<br>Products<br>Recipes<br>Contact</div>

    <div class="abs divider" style="left:913px;top:135px"></div>

    <div class="abs partner" style="left:975px;top:92px;width:113px;text-align:right;font-size:20px">post vane</div>
    <div class="abs partner" style="left:975px;top:190px;width:113px;text-align:right;font-size:24px">paylune</div>
  </div>
  <div class="abs copyright">Copyright ©2023 Brindlewood Farms. All Rights Reserved.</div>
</footer>

</body>
</html>
```